Business Card Design

Carl Brennow Insurance Agency, an Independent Insurance Agency which was stated on Pellham Row in Laplace, Louisiana on 1958 and has grown the six locations throughout South Louisiana. We sell personal (auto Homeowners flood, liability) and commercial insurance (commercial property, general liability, workers compensation, commercial auto). I am looking for a double sided card with list the five remaining locations on the back or maybe even a folded four sided card. Our home office is a two story building with a green roof. I have had a logo designed which I have attached. Open for revisions but would like to stay with in the same green roof over an M. I have attached the logo but can not tell if I was uploaded.

Target Market(s)

Individual and commercial insurance buyers. Upper income and business owners

Industry/Entity Type

Insurance

Requirements
Must have
• Must have similar logo as uploaded. Green roof over M or something similar. List all location address and phone numbers.

Employee name, office phone number; direct phone line; email address and website list all locations on card. Very Similar colors to current logo.
Nice to have
• Possible folded card with double sided print

```html
<!DOCTYPE html>
<html lang="en">
<head>
<meta charset="utf-8">
<title>Carl Brennow Insurance Agency – Business Card</title>
<link href="https://fonts.googleapis.com/css2?family=Saira:wght@400;800&family=Michroma&display=swap" rel="stylesheet">
<style>
  :root {
    --backdrop: #e4e5e6;
    --card: #ffffff;
    --agency-green: #234c3e;
    --agency-blue: #2260a8;
    --tagline-grey: #3d5a7a;
    --text-light: #ffffff;
  }
  * { margin: 0; padding: 0; box-sizing: border-box; }
  html, body {
    width: 1200px;
    height: 771px;
    overflow: hidden;
    background: var(--backdrop);
  }
  .canvas {
    position: relative;
    width: 1200px;
    height: 771px;
  }
  .card {
    position: absolute;
    top: 231px;
    width: 540px;
    height: 309px;
    background: var(--card);
    overflow: hidden;
    box-shadow: 0 2px 6px rgba(0,0,0,0.12);
  }
  .card--front { left: 40px; }
  .card--back { left: 620px; }

  /* Agency name block */
  .agency {
    position: absolute;
    display: flex;
    align-items: flex-start;
    gap: 12px;
  }
  .agency__square {
    width: 44px;
    height: 44px;
    background: var(--agency-green);
    flex: none;
    margin-top: 4px;
  }
  .agency__name {
    font-family: "Saira", sans-serif;
    font-weight: 800;
    color: var(--agency-green);
    text-transform: uppercase;
    line-height: 0.95;
    letter-spacing: 0.5px;
  }
  .agency__tagline {
    font-family: "Saira", sans-serif;
    font-weight: 800;
    color: var(--tagline-grey);
    margin-top: 4px;
    white-space: nowrap;
  }
  .card--front .agency { left: 92px; top: 112px; }
  .card--front .agency__name { font-size: 27px; }
  .card--front .agency__tagline { font-size: 13px; }

  .card--back .agency { left: 212px; top: 34px; }
  .card--back .agency__square { width: 36px; height: 36px; }
  .card--back .agency__name { font-size: 23px; }
  .card--back .agency__tagline { font-size: 10.5px; }

  /* Back: green band */
  .band {
    position: absolute;
    inset: 0;
    width: 540px;
    height: 309px;
  }
  .band__fill { fill: var(--agency-green); }
  .band__swoosh { fill: var(--agency-blue); }

  .contact-list {
    position: absolute;
    left: 26px;
    top: 118px;
    list-style: none;
    font-family: "Michroma", sans-serif;
    font-size: 7.5px;
    letter-spacing: 0.8px;
    color: var(--text-light);
  }
  .contact-list li {
    display: flex;
    align-items: center;
    gap: 7px;
    height: 14px;
  }
  .contact-list svg { width: 10px; height: 10px; flex: none; }
  .contact-list .icon-disc { fill: var(--text-light); }
  .contact-list .icon-mark { fill: var(--agency-green); stroke: var(--agency-green); }

  .holder {
    position: absolute;
    right: 26px;
    bottom: 26px;
    text-align: right;
    font-family: "Michroma", sans-serif;
    color: var(--text-light);
  }
  .holder__name { font-size: 11px; letter-spacing: 2.5px; text-transform: uppercase; }
  .holder__title { font-size: 7.5px; letter-spacing: 3px; margin-top: 4px; }
</style>
</head>
<body>
<main class="canvas">

  <section class="card card--front" aria-label="Card front">
    <div class="agency">
      <span class="agency__square"></span>
      <div>
        <div class="agency__name">Carl Brennow<br>Insurance Agency</div>
        <div class="agency__tagline">Independent Insurance for South Louisiana</div>
      </div>
    </div>
  </section>

  <section class="card card--back" aria-label="Card back">
    <svg class="band" viewBox="0 0 540 309" aria-hidden="true">
      <path class="band__fill" d="M0,86 C120,98 250,122 360,170 C430,200 490,222 540,228 L540,309 L0,309 Z"/>
      <path class="band__swoosh" d="M0,70 C130,78 260,104 360,150 C395,166 430,182 470,196 C425,176 390,160 356,147 C255,108 130,86 0,80 Z"/>
    </svg>

    <div class="agency">
      <span class="agency__square"></span>
      <div>
        <div class="agency__name">Carl Brennow<br>Insurance Agency</div>
        <div class="agency__tagline">Independent Insurance for South Louisiana</div>
      </div>
    </div>

    <ul class="contact-list">
      <li>
        <svg viewBox="0 0 10 10"><circle class="icon-disc" cx="5" cy="5" r="5"/><path class="icon-mark" d="M5,2.2a1.8,1.8 0 0 1 1.8,1.8c0,1.3-1.8,3.6-1.8,3.6s-1.8-2.3-1.8-3.6A1.8,1.8 0 0 1 5,2.2z"/></svg>
        Suite # 214, Levee Bldg.
      </li>
      <li>
        <svg viewBox="0 0 10 10"><circle class="icon-disc" cx="5" cy="5" r="5"/></svg>
        LA 70068
      </li>
      <li>
        <svg viewBox="0 0 10 10"><circle class="icon-disc" cx="5" cy="5" r="5"/><path class="icon-mark" d="M3,2.5h1.2l0.6,1.5-0.8,0.6a4,4 0 0 0 1.4,1.4l0.6-0.8 1.5,0.6v1.2c-2.6,0.3-4.8-1.9-4.5-4.5z"/></svg>
        985-555-0142
      </li>
      <li>
        <svg viewBox="0 0 10 10"><circle class="icon-disc" cx="5" cy="5" r="5"/><rect class="icon-mark" x="3" y="3.2" width="4" height="3.6"/></svg>
        985-555-0187
      </li>
      <li>
        <svg viewBox="0 0 10 10"><circle class="icon-disc" cx="5" cy="5" r="5"/><rect class="icon-mark" x="3.6" y="2.4" width="2.8" height="5.2" rx="0.5"/></svg>
        985-555-0163
      </li>
      <li>
        <svg viewBox="0 0 10 10"><circle class="icon-disc" cx="5" cy="5" r="5"/><rect class="icon-mark" x="2.6" y="3.2" width="4.8" height="3.6"/></svg>
        marcus@brennowagency.com
      </li>
      <li>
        <svg viewBox="0 0 10 10"><circle class="icon-disc" cx="5" cy="5" r="5"/><circle class="icon-mark" cx="5" cy="5" r="2.4" fill="none" stroke-width="0.8"/></svg>
        www.brennowagency.com
      </li>
    </ul>

    <div class="holder">
      <div class="holder__name">Marcus Hale</div>
      <div class="holder__title">OWNER / C.E.O</div>
    </div>
  </section>

</main>
</body>
</html>
```